Design blogshop facebook and logo

Design logo and blog shop facebook design.
Reference https://www.pagevault.example/Pellu-Vandirk-527061983314702/?ref=ts&fref=ts
Want a more trendy elegant and fashionable design for the logo and facebook

Industry/Entity Type

Shop

Colors
ffffff
ec1f27
f68d4d

```html
<!DOCTYPE html>
<html lang="en">
<head>
<meta charset="utf-8">
<title>Pellu-Vandirk — Cover</title>
<link rel="stylesheet" href="https://fonts.googleapis.com/css2?family=Cinzel:wght@500&display=swap">
<style>
  :root {
    --white: #ffffff;
    --brand-red: #ec1f27;
    --brand-peach: #f68d4d;
    --magenta: #c0146a;
    --magenta-bright: #e0207e;
    --magenta-deep: #5a0c42;
    --plum: #2a0520;
    --lens-black: #0b0b0d;
    --lens-steel: #55555c;
    --lens-ring: #1c1c20;
    --photo-orange: #e8702c;
    --photo-amber: #f29a45;
    --photo-violet: #8c3fb8;
    --photo-lilac: #b27ad0;
    --photo-denim: #6f86a8;
    --photo-wood: #a89590;
    --photo-pink: #eaa3d2;
    --photo-hot-pink: #e0489e;
    --photo-blush: #f5dbe8;
    --photo-rose: #d63f93;
    --photo-navy: #1f2230;
    --photo-grey-wall: #a9a6a8;
    --photo-tan: #9a6b4e;
    --photo-cream: #f4ecef;
    --photo-charcoal: #3a3a40;
    --photo-silver: #9d9ba2;
  }
  html, body {
    margin: 0;
    padding: 0;
    width: 1200px;
    height: 444px;
    overflow: hidden;
    background: var(--white);
  }
  .cover {
    position: relative;
    width: 1200px;
    height: 444px;
    overflow: hidden;
  }
  .cover__collage {
    position: absolute;
    inset: 0;
    display: block;
  }
  .cover__divider {
    stroke: var(--white);
    stroke-width: 3;
    fill: none;
  }
  .cover__badge {
    position: absolute;
    left: 416px;
    top: 66px;
    width: 320px;
    height: 320px;
    filter: drop-shadow(0 6px 14px rgba(20, 0, 15, 0.45));
  }
  .badge__name {
    position: absolute;
    inset: 0;
    display: flex;
    align-items: center;
    justify-content: center;
    margin: 0;
    font-family: "Cinzel", serif;
    font-weight: 500;
    font-size: 24px;
    letter-spacing: 1.5px;
    color: var(--white);
    white-space: nowrap;
  }
</style>
</head>
<body>
<main class="cover">
  <svg class="cover__collage" width="1200" height="444" viewBox="0 0 1200 444" xmlns="http://www.w3.org/2000/svg">
    <defs>
      <linearGradient id="tone-denim-model" x1="0" y1="0" x2="1" y2="1">
        <stop offset="0" stop-color="var(--photo-orange)"/>
        <stop offset="0.22" stop-color="var(--photo-amber)"/>
        <stop offset="0.4" stop-color="var(--photo-violet)"/>
        <stop offset="0.58" stop-color="var(--photo-lilac)"/>
        <stop offset="0.8" stop-color="var(--photo-denim)"/>
        <stop offset="1" stop-color="var(--photo-orange)"/>
      </linearGradient>
      <linearGradient id="tone-tulle-dress" x1="0" y1="0" x2="0.7" y2="1">
        <stop offset="0" stop-color="var(--photo-wood)"/>
        <stop offset="0.4" stop-color="var(--photo-pink)"/>
        <stop offset="0.75" stop-color="var(--photo-blush)"/>
        <stop offset="1" stop-color="var(--photo-hot-pink)"/>
      </linearGradient>
      <linearGradient id="tone-hat-model" x1="0" y1="0" x2="1" y2="1">
        <stop offset="0" stop-color="var(--photo-hot-pink)"/>
        <stop offset="0.55" stop-color="var(--photo-pink)"/>
        <stop offset="1" stop-color="var(--photo-blush)"/>
      </linearGradient>
      <linearGradient id="tone-black-blouse" x1="0" y1="0" x2="1" y2="0.6">
        <stop offset="0" stop-color="var(--photo-grey-wall)"/>
        <stop offset="0.35" stop-color="var(--photo-navy)"/>
        <stop offset="0.75" stop-color="var(--photo-navy)"/>
        <stop offset="1" stop-color="var(--photo-tan)"/>
      </linearGradient>
      <linearGradient id="tone-print-dress" x1="0" y1="0" x2="1" y2="0">
        <stop offset="0" stop-color="var(--photo-blush)"/>
        <stop offset="0.35" stop-color="#ee7a5c"/>
        <stop offset="0.55" stop-color="#b04a9a"/>
        <stop offset="0.8" stop-color="var(--photo-cream)"/>
        <stop offset="1" stop-color="var(--white)"/>
      </linearGradient>
      <linearGradient id="tone-satin-belt" x1="0" y1="0" x2="0" y2="1">
        <stop offset="0" stop-color="var(--photo-cream)"/>
        <stop offset="0.38" stop-color="var(--photo-cream)"/>
        <stop offset="0.5" stop-color="var(--photo-hot-pink)"/>
        <stop offset="0.62" stop-color="var(--photo-cream)"/>
        <stop offset="1" stop-color="var(--white)"/>
      </linearGradient>
      <linearGradient id="tone-floral-dress" x1="0" y1="0" x2="1" y2="1">
        <stop offset="0" stop-color="var(--photo-rose)"/>
        <stop offset="0.5" stop-color="var(--photo-pink)"/>
        <stop offset="1" stop-color="var(--photo-blush)"/>
      </linearGradient>
      <linearGradient id="tone-corset" x1="0" y1="0" x2="1" y2="0">
        <stop offset="0" stop-color="var(--photo-cream)"/>
        <stop offset="0.3" stop-color="var(--photo-silver)"/>
        <stop offset="0.55" stop-color="var(--photo-charcoal)"/>
        <stop offset="0.8" stop-color="var(--photo-silver)"/>
        <stop offset="1" stop-color="var(--photo-cream)"/>
      </linearGradient>
      <radialGradient id="glow-magenta" cx="0.48" cy="0.5" r="0.5">
        <stop offset="0" stop-color="var(--magenta-bright)" stop-opacity="0.55"/>
        <stop offset="1" stop-color="var(--magenta-bright)" stop-opacity="0"/>
      </radialGradient>
    </defs>

    <polygon role="img" aria-label="Photo: smiling model with violet hair and denim shirt giving thumbs up" fill="url(#tone-denim-model)" points="0,0 184,0 576,444 0,444"/>
    <polygon role="img" aria-label="Photo: model in a pink tulle gown against wooden boards" fill="url(#tone-tulle-dress)" points="184,0 672,0 832,172 752,172 752,312 460,312"/>
    <polygon role="img" aria-label="Photo: model in hat and sunglasses" fill="url(#tone-hat-model)" points="672,0 928,0 1048,172 832,172"/>
    <polygon role="img" aria-label="Photo: model in a black pleated blouse" fill="url(#tone-black-blouse)" points="928,0 1200,0 1200,270 1048,172"/>
    <polygon role="img" aria-label="Photo: model in a colourful geometric print dress" fill="url(#tone-print-dress)" points="752,172 1000,172 1090,312 752,312"/>
    <polygon role="img" aria-label="Photo: white gown with pink beaded satin belt" fill="url(#tone-satin-belt)" points="1000,172 1048,172 1200,270 1200,444 1176,444 1090,312"/>
    <polygon role="img" aria-label="Photo: model in a floral summer dress" fill="url(#tone-floral-dress)" points="460,312 840,312 900,444 576,444"/>
    <polygon role="img" aria-label="Photo: grey brocade dress with black buckled belt" fill="url(#tone-corset)" points="840,312 1090,312 1176,444 900,444"/>

    <ellipse class="cover__glow" cx="600" cy="200" rx="330" ry="250" fill="url(#glow-magenta)"/>

    <g class="cover__dividers">
      <line class="cover__divider" x1="184" y1="0" x2="576" y2="444"/>
      <line class="cover__divider" x1="672" y1="0" x2="832" y2="172"/>
      <line class="cover__divider" x1="928" y1="0" x2="1048" y2="172"/>
      <line class="cover__divider" x1="1048" y1="172" x2="1200" y2="270"/>
      <line class="cover__divider" x1="752" y1="172" x2="1048" y2="172"/>
      <line class="cover__divider" x1="752" y1="172" x2="752" y2="312"/>
      <line class="cover__divider" x1="1000" y1="172" x2="1176" y2="444"/>
      <line class="cover__divider" x1="460" y1="312" x2="1090" y2="312"/>
      <line class="cover__divider" x1="840" y1="312" x2="900" y2="444"/>
    </g>
  </svg>

  <div class="cover__badge">
    <svg width="320" height="320" viewBox="0 0 320 320" xmlns="http://www.w3.org/2000/svg" aria-hidden="true">
      <defs>
        <radialGradient id="badge-glass" cx="0.5" cy="0.15" r="0.9">
          <stop offset="0" stop-color="var(--brand-red)"/>
          <stop offset="0.25" stop-color="var(--magenta)"/>
          <stop offset="0.7" stop-color="var(--magenta-deep)"/>
          <stop offset="1" stop-color="var(--plum)"/>
        </radialGradient>
        <linearGradient id="badge-rim" x1="0" y1="0" x2="1" y2="1">
          <stop offset="0" stop-color="var(--lens-steel)"/>
          <stop offset="0.3" stop-color="var(--lens-black)"/>
          <stop offset="0.7" stop-color="var(--lens-black)"/>
          <stop offset="1" stop-color="var(--lens-steel)"/>
        </linearGradient>
        <linearGradient id="badge-sheen" x1="0" y1="0" x2="0" y2="1">
          <stop offset="0" stop-color="var(--white)" stop-opacity="0.18"/>
          <stop offset="1" stop-color="var(--white)" stop-opacity="0"/>
        </linearGradient>
      </defs>
      <circle cx="160" cy="160" r="159" fill="var(--lens-black)"/>
      <circle cx="160" cy="160" r="151" fill="url(#badge-rim)"/>
      <circle cx="160" cy="160" r="140" fill="var(--lens-ring)"/>
      <circle cx="160" cy="160" r="133" fill="url(#badge-glass)"/>
      <circle cx="160" cy="160" r="122" fill="none" stroke="var(--magenta)" stroke-opacity="0.35" stroke-width="1.5"/>
      <ellipse cx="160" cy="92" rx="104" ry="58" fill="url(#badge-sheen)"/>
    </svg>
    <p class="badge__name">Pellu-Vandirk</p>
  </div>
</main>
</body>
</html>
```